Alcohol free flavoured Malt Drink Label design

we are beverage company producer our main brand is Brightwave, we are willing to produce Alcohol free flavoured Malt Drink, this product target new generation should be fresh colourful and modern, the name of the Malt drink is Zeal. so main brand is Brightwave and product name is ZEAL. the label size: 198mm X 66mm

Dear All
i changed the product name to NUR (means Crown ) this will add more ideas in the design . Thanks

```html
<!DOCTYPE html>
<html lang="en">
<head>
<meta charset="utf-8">
<title>NUR Brightwave Flavoured Malt Drink Label</title>
<link rel="stylesheet" href="https://fonts.googleapis.com/css2?family=Alfa+Slab+One&family=Michroma&family=Noto+Serif:wght@400;500&family=Oswald:wght@300&display=swap">
<style>
  :root {
    --backdrop: #e5e5e7;
    --label-black: #1c1c1a;
    --gold: #e2b43a;
    --gold-light: #f6de94;
    --gold-deep: #c99a2e;
    --ink: #1a1a1a;
    --apple: #8cc63f;
    --apple-deep: #4e8f1e;
  }
  * { margin: 0; padding: 0; box-sizing: border-box; }
  html, body { width: 1200px; height: 1181px; overflow: hidden; }
  body { background: var(--backdrop); position: relative; }

  .body-label {
    position: absolute;
    left: 330px;
    top: 250px;
    width: 460px;
    height: 720px;
  }
  .crown-art {
    position: absolute;
    left: 110px;
    top: 0;
    width: 240px;
    height: 150px;
    border-radius: 40px 40px 8px 8px;
    background: linear-gradient(180deg, var(--gold-light), var(--gold) 55%, var(--gold-deep));
    z-index: 2;
  }
  .band-top {
    position: absolute;
    left: 0; top: 90px;
    width: 100%; height: 200px;
    background: var(--label-black);
  }
  .product-name {
    position: absolute;
    left: 0; right: 0;
    top: 165px;
    text-align: center;
    font-family: "Alfa Slab One", serif;
    font-size: 110px;
    line-height: 1;
    letter-spacing: 6px;
    color: var(--gold);
    z-index: 3;
  }
  .band-gold {
    position: absolute;
    left: 0; top: 290px;
    width: 100%; height: 120px;
    background: linear-gradient(90deg, var(--gold-deep), var(--gold-light) 50%, var(--gold-deep));
    text-align: center;
    color: var(--ink);
  }
  .brand-name {
    display: block;
    margin-top: 16px;
    font-family: "Michroma", sans-serif;
    font-weight: 400;
    font-size: 40px;
    line-height: 1.1;
    letter-spacing: 1px;
  }
  .descriptor {
    display: block;
    margin-top: 6px;
    font-family: "Noto Serif", serif;
    font-weight: 500;
    font-size: 30px;
    letter-spacing: 1px;
  }
  .band-bottom {
    position: absolute;
    left: 0; top: 410px;
    width: 100%; height: 130px;
    background: var(--label-black);
  }
  .flavour-badge {
    position: absolute;
    left: 110px;
    top: 430px;
    width: 240px;
    height: 240px;
  }

  .neck-label {
    position: absolute;
    left: 880px;
    top: 380px;
    width: 210px;
    height: 250px;
    background: linear-gradient(90deg, var(--gold-deep), var(--gold-light) 50%, var(--gold-deep));
    color: var(--ink);
  }
  .neck-brand {
    position: absolute;
    left: 105px;
    top: 95px;
    transform: translate(-50%, -50%) rotate(-90deg);
    font-family: "Michroma", sans-serif;
    font-size: 24px;
    white-space: nowrap;
  }
  .neck-descriptor {
    position: absolute;
    left: 0; right: 0;
    bottom: 18px;
    text-align: center;
    font-family: "Oswald", sans-serif;
    font-weight: 300;
    font-size: 19px;
  }
  .neck-rule {
    position: absolute;
    left: 0; right: 0; bottom: 0;
    height: 8px;
    background: var(--label-black);
  }
</style>
</head>
<body>
  <section class="body-label">
    <div class="band-top"></div>
    <div class="crown-art" role="img" aria-label="Gold crown illustration"></div>
    <div class="product-name">NUR</div>
    <div class="band-gold">
      <span class="brand-name">BRIGHTWAVE</span>
      <span class="descriptor">Flavoured Malt Drink</span>
    </div>
    <div class="band-bottom"></div>
    <svg class="flavour-badge" viewBox="0 0 240 240" aria-label="Green apple flavour badge">
      <defs>
        <linearGradient id="ring-gold" x1="0" y1="0" x2="1" y2="1">
          <stop offset="0" stop-color="#f6de94"/>
          <stop offset="0.5" stop-color="#e2b43a"/>
          <stop offset="1" stop-color="#c99a2e"/>
        </linearGradient>
        <radialGradient id="apple-tone" cx="0.4" cy="0.35" r="0.7">
          <stop offset="0" stop-color="#c8e68a"/>
          <stop offset="0.6" stop-color="#8cc63f"/>
          <stop offset="1" stop-color="#4e8f1e"/>
        </radialGradient>
        <path id="arc-top" d="M 40 120 A 80 80 0 0 1 200 120"/>
        <path id="arc-bottom" d="M 32 120 A 88 88 0 0 0 208 120"/>
      </defs>
      <circle cx="120" cy="120" r="114" fill="#1c1c1a" stroke="url(#ring-gold)" stroke-width="6"/>
      <circle cx="120" cy="120" r="104" fill="none" stroke="url(#ring-gold)" stroke-width="1.5"/>
      <text font-family="Noto Serif, serif" font-size="26" fill="#e2b43a" letter-spacing="3">
        <textPath href="#arc-top" startOffset="50%" text-anchor="middle">FLAVOURED</textPath>
      </text>
      <text font-family="Noto Serif, serif" font-size="22" fill="#e2b43a" letter-spacing="2">
        <textPath href="#arc-bottom" startOffset="50%" text-anchor="middle">Green Appel</textPath>
      </text>
      <circle cx="120" cy="118" r="40" fill="url(#apple-tone)" role="img" aria-label="Green apple illustration"/>
    </svg>
  </section>

  <aside class="neck-label">
    <span class="neck-brand">Brightwave</span>
    <span class="neck-descriptor">Flavoured Malt Drink</span>
    <span class="neck-rule"></span>
  </aside>
</body>
</html>
```